Talvero Engineering & Management Services Website

A professional website design that outlines Engineering and Management Services. The website is to be colour coordinated with the current logo (see attached). The webpage needs to be compatible with Wordpress to allow for easy changes to be made to the website for the user.
Required tabs for the page include:
- Civil Engineering
- Structural Engineering
- Project Management
- Business Management
- Project Controls
- Drafting
- Contact Us

Clean and efficient website that matches the services provided by the business.

Target Market(s)

New Customers to a very competitive market

Industry/Entity Type

Engineering

Number of Pages Required

5+ page

Requirements
Must have
• Clean with large stock photos

```html
<!DOCTYPE html>
<html lang="en">
<head>
<meta charset="utf-8">
<title>Talvero Engineering &amp; Management Services</title>
<link href="https://fonts.googleapis.com/css2?family=Raleway:wght@400;600;700;800&family=Open+Sans:wght@400;600;700&display=swap" rel="stylesheet">
<style>
:root{
  --orange:#f26b21;
  --orange-dark:#c9521a;
  --ink:#2b2b2b;
  --text:#555;
  --muted:#8a8a8a;
  --band:#eeeeee;
  --line:#dddddd;
  --footer-dark:#2a2a2a;
  --white:#fff;
}
*{box-sizing:border-box;margin:0;padding:0}
html,body{width:1200px;height:2256px;overflow:hidden}
body{background:var(--white);font-family:"Open Sans",Arial,sans-serif;color:var(--text);position:relative}
.wrap{width:1040px;margin:0 auto;position:relative}
h1,h2,h3,h4{font-family:"Raleway",Arial,sans-serif}

/* header */
.site-header{height:120px}
.site-header .wrap{height:120px;display:flex;align-items:center;justify-content:space-between}
.brand{display:flex;align-items:center;gap:14px}
.brand-dot{width:52px;height:52px;border-radius:50%;background:var(--orange)}
.brand-name{font-family:"Raleway",sans-serif;font-weight:800;font-size:30px;color:var(--ink);letter-spacing:1px}
.brand-sub{display:block;font-size:11px;font-weight:800;letter-spacing:1.4px;color:var(--ink);text-transform:uppercase;margin-top:2px}
.phone{display:flex;align-items:center;gap:12px;font-family:"Raleway",sans-serif;font-weight:700;font-size:26px;color:var(--ink)}

/* nav */
.main-nav{height:48px;background:var(--orange)}
.main-nav ul{list-style:none;display:flex;height:48px;width:1040px;margin:0 auto}
.main-nav li{display:flex;align-items:center;padding:0 16px;font-size:13px;color:var(--white)}
.main-nav li.active{background:var(--orange-dark)}

/* hero */
.hero{position:relative;height:632px;overflow:hidden}
.hero-photo{position:absolute;inset:0;background:linear-gradient(100deg,#f2f2f0 0%,#d9dad8 35%,#8e949a 60%,#3f4650 85%,#2d3138 100%)}
.hero-text{position:absolute;left:80px;top:248px}
.hero-text h1{font-size:44px;font-weight:600;line-height:1.15;color:var(--ink);text-transform:uppercase}
.hero-text h1 span{color:var(--orange);display:block}
.hero-arrows{position:absolute;left:80px;top:390px;display:flex;gap:6px}
.hero-arrows span{width:30px;height:30px;background:#555;display:flex;align-items:center;justify-content:center}
.hero-arrows span.next{background:var(--orange)}
.hero-dots{position:absolute;left:50%;bottom:24px;transform:translateX(-50%);display:flex;gap:8px}
.hero-dots i{width:10px;height:10px;border-radius:50%;background:rgba(255,255,255,.6)}
.hero-dots i.on{background:var(--orange)}

/* welcome */
.welcome{height:192px;padding-top:52px;text-align:center}
.welcome h2{font-size:28px;font-weight:700;color:var(--ink);text-transform:uppercase}
.welcome h2 span{color:var(--orange)}
.welcome p{width:1040px;margin:20px auto 0;font-size:14px;line-height:22px;text-align:left;color:var(--text)}

/* services */
.services{background:var(--band);height:340px;padding-top:28px}
.section-head{display:flex;justify-content:space-between;align-items:center;margin-bottom:20px}
.section-head h3{font-size:22px;font-weight:700;color:var(--ink);text-transform:uppercase}
.section-head h3 span{color:var(--orange)}
.pager{display:flex;gap:12px}
.cards{display:flex;gap:32px;padding:0 8px}
.card{width:320px;background:var(--white);padding:6px 6px 0}
.card-photo{height:196px}
.card h4{font-size:13px;font-weight:700;text-align:center;padding:12px 0;color:var(--ink);text-transform:uppercase}
.p1{background:linear-gradient(160deg,#b6cde0,#8aa7c0 50%,#6e7a86)}
.p2{background:linear-gradient(160deg,#e7e7e4,#b9bcbf 55%,#7d8489)}
.p3{background:linear-gradient(160deg,#dfe7ee,#cfcfcb 50%,#e0a050)}

/* about block */
.about{height:360px;padding-top:48px}
.about .wrap{display:flex;gap:40px}
.about-photo{width:400px;height:260px;flex:none;border:6px solid #f4f4f4;background:linear-gradient(150deg,#f4f4f2,#d8dbdd 55%,#aab4bd)}
.about-body{padding-top:18px}
.about-body h3{font-size:22px;font-weight:700;color:var(--ink);text-transform:uppercase}
.about-body h3 span{color:var(--orange)}
.about-body p{font-size:13px;line-height:20px;margin-top:14px}
.btn{display:inline-block;margin-top:20px;background:var(--orange);color:var(--white);font-size:13px;font-weight:600;padding:10px 22px}

/* news */
.news{height:276px;padding-top:8px}
.news-items{display:flex;gap:40px}
.news-item{width:500px;display:flex;gap:20px}
.news-photo{width:180px;height:140px;flex:none}
.n1{background:linear-gradient(150deg,#d7e2ec,#9fb4c7 50%,#5c6b7a)}
.n2{background:linear-gradient(150deg,#c4d6e6,#e8c14a 45%,#6f7c88)}
.news-item h4{font-size:13px;font-weight:700;color:var(--orange);text-transform:uppercase}
.news-item p{font-size:12px;line-height:19px;margin-top:8px}
.news-item a{display:block;margin-top:8px;font-size:12px;color:var(--orange);text-decoration:none}

/* footer */
.site-footer{background:var(--orange);height:212px;padding-top:44px}
.foot-cols{display:flex;justify-content:space-between}
.foot-col{width:190px;color:var(--white)}
.foot-col h5{font-family:"Raleway",sans-serif;font-size:14px;font-weight:700;text-transform:uppercase;margin-bottom:14px}
.foot-col li{list-style:none;font-size:12px;line-height:22px}
.copyright{background:var(--footer-dark);height:76px;display:flex;align-items:center;justify-content:center;font-size:12px;color:#bbb;position:relative}
.copyright .up{position:absolute;right:80px;top:30px}
</style>
</head>
<body>

<header class="site-header">
  <div class="wrap">
    <div class="brand">
      <span class="brand-dot"></span>
      <div class="brand-name">TALVERO<span class="brand-sub">Engineering &amp; Management Services</span></div>
    </div>
    <div class="phone">
      <svg width="30" height="30" viewBox="0 0 24 24"><circle cx="12" cy="12" r="12" fill="#f26b21"/><path d="M8.5 6.5l2 .2.8 2.6-1.3 1c.7 1.5 1.9 2.7 3.4 3.4l1-1.3 2.6.8.2 2c-.2.8-.9 1.3-1.7 1.3A9.6 9.6 0 0 1 7.2 8.2c0-.8.5-1.5 1.3-1.7z" fill="#fff"/></svg>
      + 8 800 555 01 84
    </div>
  </div>
</header>

<nav class="main-nav">
  <ul>
    <li class="active">Home</li>
    <li>About Us</li>
    <li>Civil Engineering</li>
    <li>Structural Engineering</li>
    <li>Project Management</li>
    <li>Business Management</li>
    <li>Project Controls</li>
    <li>Drafting</li>
    <li>Contact Us</li>
  </ul>
</nav>

<section class="hero">
  <div class="hero-photo" role="img" aria-label="Stock photo of engineers discussing plans at an office desk"></div>
  <div class="hero-text">
    <h1>Engineering and<span>Management Services</span></h1>
  </div>
  <div class="hero-arrows">
    <span><svg width="12" height="12" viewBox="0 0 12 12"><path d="M8 1L3 6l5 5" stroke="#fff" stroke-width="2" fill="none"/></svg></span>
    <span class="next"><svg width="12" height="12" viewBox="0 0 12 12"><path d="M4 1l5 5-5 5" stroke="#fff" stroke-width="2" fill="none"/></svg></span>
  </div>
  <div class="hero-dots"><i class="on"></i><i></i><i></i></div>
</section>

<section class="welcome">
  <h2>Welcome to <span>Talvero</span></h2>
  <p>Lorem Ipsum has been the industry's standard dummy text ever since the 1500s, when an unknown printer took a galley of type and scrambled it to make a type specimen book. It has survived not only five centuries, but also the leap into electronic typesetting, remaining essentially unchanged</p>
</section>

<section class="services">
  <div class="wrap">
    <div class="section-head">
      <h3>Our <span>Service</span></h3>
      <div class="pager">
        <svg width="12" height="14" viewBox="0 0 12 14"><path d="M9 1L3 7l6 6" stroke="#555" stroke-width="2" fill="none"/></svg>
        <svg width="12" height="14" viewBox="0 0 12 14"><path d="M3 1l6 6-6 6" stroke="#555" stroke-width="2" fill="none"/></svg>
      </div>
    </div>
    <div class="cards">
      <div class="card"><div class="card-photo p1" role="img" aria-label="Photo of civil engineers on a construction site"></div><h4>Civil Engineering</h4></div>
      <div class="card"><div class="card-photo p2" role="img" aria-label="Photo of structural drawings being reviewed"></div><h4>Structural Engineering</h4></div>
      <div class="card"><div class="card-photo p3" role="img" aria-label="Photo of a project team in hard hats"></div><h4>Project Management</h4></div>
    </div>
  </div>
</section>

<section class="about">
  <div class="wrap">
    <div class="about-photo" role="img" aria-label="Photo of hands drafting a technical plan"></div>
    <div class="about-body">
      <h3>Engineering and <span>Management Services</span></h3>
      <p>Our engineering and management team delivers practical, safe and efficient results on every site. We pair years of field experience with modern planning tools, so each project is measured, tracked and finished on time and within the agreed budget.</p>
      <p>If you are unsure which service fits your project, call our office or send a short message and we will review your plans.</p>
      <span class="btn">Read More</span>
    </div>
  </div>
</section>

<section class="news">
  <div class="wrap">
    <div class="section-head">
      <h3>Latest <span>News</span></h3>
      <div class="pager">
        <svg width="12" height="14" viewBox="0 0 12 14"><path d="M9 1L3 7l6 6" stroke="#555" stroke-width="2" fill="none"/></svg>
        <svg width="12" height="14" viewBox="0 0 12 14"><path d="M3 1l6 6-6 6" stroke="#555" stroke-width="2" fill="none"/></svg>
      </div>
    </div>
    <div class="news-items">
      <article class="news-item">
        <div class="news-photo n1" role="img" aria-label="Photo of a business meeting"></div>
        <div><h4>Simply Dummy Text</h4><p>Our site team completed the foundation survey for a new public library ahead of schedule, with full reports shared with the client the same week.</p><a>Read More »</a></div>
      </article>
      <article class="news-item">
        <div class="news-photo n2" role="img" aria-label="Photo of engineers in hard hats on site"></div>
        <div><h4>Simply Dummy Text</h4><p>Structural checks on the riverside warehouse are finished, and the project controls group has issued the final cost and progress summary to the owner.</p><a>Read More »</a></div>
      </article>
    </div>
  </div>
</section>

<footer class="site-footer">
  <div class="wrap foot-cols">
    <div class="foot-col"><h5>Link</h5><ul><li>Home</li><li>About Us</li><li>Presentation</li></ul></div>
    <div class="foot-col"><h5>Specialists</h5><ul><li>Services</li><li>Employees</li><li>Technology</li></ul></div>
    <div class="foot-col"><h5>Service</h5><ul><li>FAQs</li><li>Support</li></ul></div>
    <div class="foot-col"><h5>Address</h5><ul><li>Sign Up</li><li>Careers</li><li>Promotions</li></ul></div>
    <div class="foot-col"><h5>Contact Us</h5><ul><li>22 Harbor Lane, Westbrook, Australia</li><li>Phone: +61 2 5550 0193</li><li>Email: info@talvero.com</li></ul></div>
  </div>
</footer>
<div class="copyright">Copyright © 2014 . All Rights Reserved.
  <svg class="up" width="14" height="10" viewBox="0 0 14 10"><path d="M1 9l6-7 6 7" stroke="#bbb" stroke-width="2" fill="none"/></svg>
</div>

</body>
</html>
```